Public Speaking Book for aspiring, ambitious speakers

I'm looking for a 6x9 book cover (Parcelo standard) as well as ebook and audiobook formats.

I'm looking for orange font on a white background as these are my brand colours.

Feel free to use some yellow and gold too if you deem it appropriate.

Title: Climb and Glow
Subtitle: Find Your Voice. Tell Your Story. Share your Message.
Author: Lionel Barstow

I would like to have a picture of a female speaker on the front cover.

Alternatively, some kind of image that symbolises public speaking like a microphone, podium etc

Target Market(s)

Aspiring professional speakers

Colors
f78f20

Requirements
Must have
• Correct spelling!
Nice to have
• A logo or picture that fits the theme, but no pressure if you can't think of anything
Should not have
• No men in suits please. I don't want this to have a 1980s corporate look.

```html
<!DOCTYPE html>
<html lang="en">
<head>
<meta charset="utf-8">
<title>Climb and Glow – Full Cover</title>
<link href="https://fonts.googleapis.com/css2?family=Oswald:wght@400;500;600;700&family=Open+Sans:wght@400;600&display=swap" rel="stylesheet">
<style>
  :root {
    --brand-orange: #f78f20;
    --paper: #ffffff;
    --stage: #eeeeee;
    --ink: #6b6b6b;
    --ink-dark: #4a4a4a;
    --wood-light: #a9714a;
    --wood-dark: #6e4328;
    --mic-silver: #c9c9c9;
    --mic-dark: #6a6a6a;
  }
  * { box-sizing: border-box; margin: 0; padding: 0; }
  html, body { width: 745px; height: 1200px; overflow: hidden; }
  body {
    background: var(--stage);
    font-family: "Open Sans", Arial, sans-serif;
    position: relative;
  }
  .cover-wrap {
    position: absolute;
    left: 20px; top: 352px;
    width: 705px; height: 495px;
    display: flex;
    background: var(--paper);
    box-shadow: 0 2px 10px rgba(0,0,0,.15);
  }
  .panel { position: relative; height: 100%; overflow: hidden; }
  .back-cover { width: 330px; }
  .spine { width: 45px; border-left: 1px solid #e4e4e4; border-right: 1px solid #e4e4e4; }
  .front-cover { width: 330px; }

  .wood-band {
    position: absolute; left: 0; right: 0; bottom: 0; height: 42px;
    background: linear-gradient(180deg, var(--wood-light), var(--wood-dark));
  }

  /* Back cover */
  .back-header { position: absolute; left: 16px; top: 18px; display: flex; align-items: flex-end; gap: 8px; }
  .mic-art-small {
    width: 26px; height: 58px;
    background: linear-gradient(180deg, var(--mic-silver), var(--mic-dark));
    border-radius: 12px 12px 3px 3px;
  }
  .back-title {
    font-family: "Oswald", Arial, sans-serif; font-weight: 700;
    color: var(--brand-orange); font-size: 34px; line-height: 1; letter-spacing: .5px;
  }
  .back-title small { font-size: 16px; font-weight: 600; letter-spacing: 1px; }
  .blurb { position: absolute; left: 18px; right: 22px; top: 96px; }
  .blurb p {
    font-size: 8.5px; line-height: 1.55; color: var(--ink); margin-bottom: 10px;
  }
  .author-note { position: absolute; left: 18px; right: 22px; bottom: 54px; display: flex; gap: 10px; align-items: flex-start; }
  .author-square { flex: 0 0 58px; height: 58px; background: var(--brand-orange); }
  .author-note p { font-size: 8.5px; line-height: 1.55; color: var(--ink); }

  /* Spine */
  .spine-text {
    position: absolute; left: 50%; top: 16px;
    transform: translateX(-50%);
    writing-mode: vertical-rl;
    font-family: "Oswald", Arial, sans-serif;
    display: flex; align-items: center; gap: 0;
    height: 420px; justify-content: space-between;
  }
  .spine-title { color: var(--brand-orange); font-weight: 700; font-size: 18px; letter-spacing: 4px; }
  .spine-author { color: var(--ink-dark); font-weight: 500; font-size: 13px; letter-spacing: 1px; }

  /* Front cover */
  .front-title {
    position: absolute; left: 22px; top: 26px;
    font-family: "Oswald", Arial, sans-serif; font-weight: 700;
    color: var(--brand-orange); text-transform: uppercase; line-height: .95;
  }
  .front-title .big { display: block; font-size: 92px; letter-spacing: 1px; }
  .front-title .joiner { display: block; font-size: 34px; font-weight: 600; letter-spacing: 14px; margin: 4px 0 6px; }
  .subtitle {
    position: absolute; left: 24px; top: 306px;
    font-size: 19px; line-height: 1.2; color: var(--ink); font-family: "Open Sans", Arial, sans-serif;
  }
  .mic-art {
    position: absolute; right: 22px; top: 290px; width: 54px; height: 163px;
    background: linear-gradient(180deg, var(--mic-silver), var(--mic-dark));
    border-radius: 24px 24px 4px 4px;
  }
  .front-author {
    position: absolute; left: 24px; bottom: 52px;
    font-family: "Oswald", Arial, sans-serif; font-weight: 500;
    font-size: 17px; color: var(--ink-dark); letter-spacing: 1px; text-transform: uppercase;
  }
</style>
</head>
<body>
  <main class="cover-wrap">
    <section class="panel back-cover">
      <div class="back-header">
        <div class="mic-art-small" role="img" aria-label="Vintage studio microphone"></div>
        <div class="back-title">CLIMB <small>AND GLOW</small></div>
      </div>
      <div class="blurb">
        <p>Step onto any stage with calm and purpose. This book shows how to shape your ideas, steady your nerves and speak so people lean in and listen.</p>
        <p>Each chapter pairs a simple habit with a short exercise, from finding your core message to telling stories that stay with an audience long after you finish.</p>
        <p>Whether you speak at meetings, events or online, you will gain tools to grow.</p>
        <p>Written for new and rising speakers who want to turn a quiet idea into a clear voice, one talk at a time.</p>
      </div>
      <div class="author-note">
        <div class="author-square"></div>
        <p>About the author: a coach who helps people share their message with warmth and confidence.</p>
      </div>
      <div class="wood-band" role="img" aria-label="Warm wooden stage floor texture"></div>
    </section>

    <section class="panel spine">
      <div class="spine-text">
        <span class="spine-title">CLIMB AND GLOW</span>
        <span class="spine-author">LIONEL BARSTOW</span>
      </div>
      <div class="wood-band" role="img" aria-label="Warm wooden stage floor texture"></div>
    </section>

    <section class="panel front-cover">
      <h1 class="front-title">
        <span class="big">Climb</span>
        <span class="joiner">and</span>
        <span class="big">Glow</span>
      </h1>
      <p class="subtitle">Find Your Voice.<br>Tell Your Story.<br>Share your Message.</p>
      <div class="mic-art" role="img" aria-label="Vintage studio microphone on a stand"></div>
      <p class="front-author">Lionel Barstow</p>
      <div class="wood-band" role="img" aria-label="Warm wooden stage floor texture"></div>
    </section>
  </main>
</body>
</html>
```